new ownership of a business

Tax & accounting firm including payroll processing, business consulting, bookkeeping
I am a new owner and want to inform current clients I want the announcement to be subtle. something like "same friendly faces, brand new name" the name is going from "Wendell R. Pickett, CPA, PC" to "Pickett Marlowe & Associates, LLC" I would like to emphasize a little on the Marlowe part of the name. I would like the words "Tax Accountants" below the name.
Accounting

```html
<!DOCTYPE html>
<html lang="en">
<head>
<meta charset="utf-8">
<title>Pickett Marlowe &amp; Associates, LLC — Same Friendly Faces, Brand New Name</title>
<link href="https://fonts.googleapis.com/css2?family=Bitter:wght@400;700&family=Open+Sans:wght@400;600&display=swap" rel="stylesheet">
<style>
  :root {
    --brand-blue: #1a73c0;
    --ink-grey: #4a4a4a;
    --text-dark: #2b2b2b;
    --soft-grey: #b4b7bb;
    --paper: #ffffff;
  }
  * { margin: 0; padding: 0; box-sizing: border-box; }
  html, body { width: 1200px; height: 954px; overflow: hidden; background: var(--paper); }
  .flyer {
    position: relative;
    width: 1200px; height: 954px;
    background: var(--paper);
    overflow: hidden;
    font-family: "Open Sans", Arial, sans-serif;
  }
  .flyer__waves { position: absolute; inset: 0; width: 1200px; height: 954px; }
  .headline {
    position: absolute; left: 64px; top: 48px;
    font-family: "Bitter", Georgia, serif; font-weight: 400;
    font-size: 56px; line-height: 1.28;
  }
  .headline__lead { color: var(--brand-blue); display: block; }
  .headline__sub { color: var(--ink-grey); display: block; }
  .firm-type {
    position: absolute; left: 64px; top: 248px;
    font-family: "Bitter", Georgia, serif; font-weight: 400;
    font-size: 34px; letter-spacing: 1px; color: var(--brand-blue);
  }
  .services {
    position: absolute; left: 64px; top: 316px;
    list-style: none; font-size: 33px; color: var(--text-dark); line-height: 45px;
  }
  .services li { display: flex; align-items: center; gap: 14px; }
  .services svg { width: 28px; height: 28px; flex: none; }
  .illustration {
    position: absolute; left: 372px; top: 430px; width: 225px; height: 185px;
    border-radius: 14px;
    background: linear-gradient(135deg, #f1e2c4 0%, #d9b98a 55%, #6a6f77 100%);
  }
  .portrait {
    position: absolute; left: 605px; top: 75px; width: 540px; height: 540px;
    border-radius: 50%;
    background: radial-gradient(circle at 45% 32%, #e9d3c2 0%, #c9b3a3 20%, #2a3550 46%, #1c2438 78%, #d9dde3 100%);
  }
  .transition {
    position: absolute; left: 200px; width: 890px; top: 660px;
    text-align: center;
  }
  .transition__from { font-size: 33px; line-height: 46px; color: var(--ink-grey); }
  .transition__name {
    font-family: "Bitter", Georgia, serif; font-weight: 700;
    font-size: 43px; line-height: 56px; color: var(--brand-blue);
  }
  .transition__tag { font-size: 33px; line-height: 46px; color: var(--brand-blue); }
  .contact {
    position: absolute; left: 0; right: 0; top: 890px;
    display: flex; justify-content: center; gap: 120px;
    font-size: 35px; line-height: 48px; color: #ffffff;
  }
  .contact span { display: flex; align-items: center; gap: 8px; }
  .contact svg { width: 34px; height: 34px; }
</style>
</head>
<body>
<main class="flyer">
  <svg class="flyer__waves" viewBox="0 0 1200 954" aria-hidden="true">
    <path d="M0,575 C140,550 290,560 350,605 C250,600 170,660 200,765 C250,875 690,885 900,830 C1050,790 1150,740 1200,700 L1200,954 L0,954 Z" fill="var(--brand-blue)"/>
    <path d="M0,560 C140,536 290,546 352,592" fill="none" stroke="var(--soft-grey)" stroke-width="5"/>
    <path d="M226,680 C214,830 680,872 900,815 C1050,778 1150,728 1200,688" fill="none" stroke="var(--soft-grey)" stroke-width="10"/>
    <path d="M1154,296 A283,283 0 0 1 778,611" fill="none" stroke="var(--soft-grey)" stroke-width="7"/>
  </svg>

  <h1 class="headline">
    <span class="headline__lead">Same Friendly Faces,</span>
    <span class="headline__sub">Brand New Name</span>
  </h1>

  <h2 class="firm-type">TAX &amp; ACCOUNTING FIRM</h2>

  <ul class="services">
    <li><svg viewBox="0 0 28 28"><circle cx="14" cy="14" r="11" fill="none" stroke="var(--brand-blue)" stroke-width="3"/><path d="M8,14 l5,5 l10,-12" fill="none" stroke="var(--brand-blue)" stroke-width="3.5"/></svg>Payroll Processing</li>
    <li><svg viewBox="0 0 28 28"><circle cx="14" cy="14" r="11" fill="none" stroke="var(--brand-blue)" stroke-width="3"/><path d="M8,14 l5,5 l10,-12" fill="none" stroke="var(--brand-blue)" stroke-width="3.5"/></svg>Business Consulting</li>
    <li><svg viewBox="0 0 28 28"><circle cx="14" cy="14" r="11" fill="none" stroke="var(--brand-blue)" stroke-width="3"/><path d="M8,14 l5,5 l10,-12" fill="none" stroke="var(--brand-blue)" stroke-width="3.5"/></svg>Bookkeeping</li>
  </ul>

  <div class="illustration" role="img" aria-label="Illustration of a clipboard with a bar chart beside a calculator"></div>

  <div class="portrait" role="img" aria-label="Photo of a smiling accountant in a dark suit and tie, with a colleague working in the office behind him"></div>

  <section class="transition">
    <p class="transition__from">from "Wendell R. Pickett, CPA, PC" to</p>
    <p class="transition__name">Pickett Marlowe &amp; Associates, LLC</p>
    <p class="transition__tag">Tax Accountants</p>
  </section>

  <footer class="contact">
    <span><svg viewBox="0 0 34 34"><circle cx="17" cy="17" r="14" fill="none" stroke="#fff" stroke-width="2.5"/><path d="M12,9 q-3,8 3,15 q4,4 8,2 l-2,-4 l-3,1 q-4,-4 -3,-9 l3,-1 z" fill="#fff"/></svg>012 555 01987</span>
    <span><svg viewBox="0 0 34 34"><rect x="3" y="8" width="28" height="19" fill="none" stroke="#fff" stroke-width="2.5"/><path d="M3,8 l14,11 l14,-11" fill="none" stroke="#fff" stroke-width="2.5"/></svg>hello@pmtax.example</span>
  </footer>
</main>
</body>
</html>
```